High end Coffee Roaster needs a Label design for new Blend

We are looking for a label design for a new blend called "Cold Brew Blend". It is a blend of coffee that we use for making cold brew coffee. The blend is sold as the whole bean and ground coffee in a bag as well as pre-brewed ready to drink in a bottle. We would like the label to be elegant but fun and It must include our logo. Please check out or website brightmillroasters.com or social media @brightmillroasters for information on our company and our coffees if you need more ideas on the kind of product we offer and our style.

Requirements
Must have
• Our Company Logo. Creative design.
Should not have
• This project should NOT be a corporate company logo, Please do NOT submit a design for a company logo this is a project for a Label. We already have a logo and we are looking for a design on a label. I have uploaded several examples of what we are looking for. Those examples are from other coffee companies who have cold brew. Those are examples only to give you a better idea of what im looking for. DO NOT COPY THEM.

```html
<!DOCTYPE html>
<html lang="en">
<head>
<meta charset="utf-8">
<title>Cold Brew Label – Bright Mill Roasters</title>
<link href="https://fonts.googleapis.com/css2?family=Oswald:wght@500&family=Montserrat:wght@600&display=swap" rel="stylesheet">
<style>
  :root {
    --stage: #f1f1f1;
    --stage-edge: #d9d9d9;
    --amber-light: #4a260f;
    --amber-dark: #2a1306;
    --print: #ffffff;
    --accent: #e39a2a;
  }
  * { margin: 0; padding: 0; box-sizing: border-box; }
  html, body { width: 1200px; height: 1000px; overflow: hidden; }
  body {
    background: radial-gradient(ellipse at center, var(--stage) 55%, var(--stage-edge) 100%);
    position: relative;
    font-family: "Montserrat", sans-serif;
  }
  .label {
    position: absolute;
    top: 230px;
    width: 280px;
    height: 570px;
    border-radius: 36px;
    background: linear-gradient(90deg, var(--amber-dark) 0%, var(--amber-light) 45%, var(--amber-dark) 100%);
    color: var(--print);
    text-align: center;
  }
  .label--colour { left: 200px; }
  .label--mono { left: 716px; }
  .label__title {
    position: absolute;
    top: 114px;
    left: 0;
    width: 100%;
    font-family: "Oswald", sans-serif;
    font-weight: 500;
    font-size: 108px;
    line-height: 100px;
    letter-spacing: 1px;
  }
  .label__title span {
    display: block;
    height: 100px;
    transform: scaleX(0.53);
  }
  .label__tagline {
    position: absolute;
    top: 325px;
    left: 59px;
    width: 168px;
    height: 29px;
    border: 2px solid var(--print);
    display: flex;
    align-items: center;
    justify-content: center;
    white-space: nowrap;
    font-family: "Oswald", sans-serif;
    font-weight: 500;
    font-size: 13px;
    letter-spacing: 0.8px;
  }
  .label__mark {
    position: absolute;
    top: 367px;
    left: 119px;
    width: 42px;
    height: 42px;
    border-radius: 50%;
    border: 3px solid var(--print);
  }
  .label--colour .label__mark { border-color: var(--accent); }
  .label__brand {
    position: absolute;
    top: 425px;
    left: 0;
    width: 100%;
    white-space: nowrap;
    font-weight: 600;
    font-size: 14px;
    letter-spacing: 0.3px;
  }
</style>
</head>
<body>
  <section class="label label--colour">
    <h1 class="label__title"><span>COLD</span><span>BREW</span></h1>
    <p class="label__tagline">PREMIUM ICED COFFEE</p>
    <div class="label__mark"></div>
    <p class="label__brand">BRIGHT MILL ROASTERS</p>
  </section>

  <section class="label label--mono">
    <h1 class="label__title"><span>COLD</span><span>BREW</span></h1>
    <p class="label__tagline">PREMIUM ICED COFFEE</p>
    <div class="label__mark"></div>
    <p class="label__brand">BRIGHT MILL ROASTERS</p>
  </section>
</body>
</html>
```